Design Some Double Sided Business Cards for a Printing Company

***WINNER WILL GET MORE BUSINESS CARD WORK AS A DIRECT HIRE***

Company is a print shop website that allows people to order printed materials such as business cards, brochures, banners, catalogs and more (like quelmocard.com). The design should include elements for a print shop.

These business cards will incorporate Silver Foil (the grey part of logo will be silver foil for sure) and also Spot UV.

*Logo is attached. One file has transparent background (PDF file) and the other has a white background (JPG file). Use which one works best with your design

*Silver Foil will be on only ONE SIDE, not both

*Spot UV will also only be on ONE SIDE, not both

Both Foil and Spot UV may be on the same side or on different sides depending on the design. Be sure to create the artwork with Foil and Spot UV in mind to increase the look of your design.

***HERE IS INFO TO USE IN YOUR DESIGN***
(Name) Tom Lark
(Title) Ambassador of Print
(Phone) 731.590.4407
(email) info@kqbprinting.com
(web) www.kqbprinting.com

*DO NOT include info inside of the ( ) above

**I need many business card designs each week and looking to build a team of designers to directly hire for this work. Winner will be added to the team. The graphic designer of other great designs will be added to the team also.

Thanks!

```html
<!DOCTYPE html>
<html lang="en">
<head>
<meta charset="utf-8">
<title>KQB Printing – Business Card</title>
<link rel="stylesheet" href="https://fonts.googleapis.com/css2?family=Montserrat:wght@400;800;900&family=Quicksand:wght@400&family=Tinos&display=swap">
<style>
  :root {
    --page: #ffffff;
    --front-bg: #0d0f14;
    --front-glow: #1b1f27;
    --bar-dark: #2a2b2f;
    --cyan: #1fb8ec;
    --headline-grey: #5c5e63;
    --tag-grey: #d6d8db;
    --back-dark: #3a3a3c;
    --back-panel: #4e4f52;
    --map-tone: #5d5e61;
    --red: #ff0000;
    --white: #ffffff;
    --brand-blue: #3a8fd1;
    --shadow: #111111;
  }
  html, body {
    margin: 0;
    width: 1200px;
    height: 1200px;
    overflow: hidden;
    background: var(--page);
  }
  .canvas { position: relative; width: 1200px; height: 1200px; }

  /* ---------- Front side ---------- */
  .card-front {
    position: absolute; left: 219px; top: 99px; width: 757px; height: 432px;
    background: radial-gradient(ellipse at 50% 40%, var(--front-glow), var(--front-bg) 75%);
    overflow: hidden;
  }
  .brand {
    position: absolute; display: flex; align-items: center; gap: 12px;
    font-family: "Montserrat", sans-serif; font-weight: 900; letter-spacing: 1px;
    white-space: nowrap;
  }
  .brand-square { width: 30px; height: 30px; background: var(--brand-blue); flex: none; }
  .card-front .brand {
    left: 0; right: 0; top: 110px; justify-content: center;
    font-size: 40px; color: var(--white);
  }
  .headline {
    position: absolute; left: 0; right: 0; top: 196px; text-align: center;
    font-family: "Montserrat", sans-serif; font-weight: 900; font-size: 86px;
    line-height: 1; color: var(--headline-grey); letter-spacing: 1px;
  }
  .tagline {
    position: absolute; left: 0; right: 0; top: 284px; text-align: center;
    font-family: "Montserrat", sans-serif; font-weight: 400; font-size: 17px;
    letter-spacing: 7px; color: var(--tag-grey);
  }
  .tagline .accent { color: var(--cyan); }
  .web-bar { position: absolute; left: 0; bottom: 0; width: 100%; height: 38px; display: flex; }
  .web-bar .cap { width: 85px; background: var(--cyan); }
  .web-bar .mid {
    flex: 1; background: var(--bar-dark); color: var(--cyan); text-align: center;
    font-family: "Quicksand", sans-serif; font-size: 31px; line-height: 38px;
  }

  /* ---------- Back side ---------- */
  .card-back {
    position: absolute; left: 219px; top: 648px; width: 761px; height: 433px;
    background: var(--back-dark); overflow: hidden;
  }
  .map-panel { position: absolute; left: 0; top: 0; }
  .card-back .brand {
    right: 40px; top: 28px; font-size: 30px; color: var(--white);
  }
  .card-back .brand .brand-square { width: 24px; height: 24px; }
  .info-bar {
    position: absolute; right: 0; height: 47px; background: var(--red);
    color: var(--white); font-family: "Tinos", serif; font-size: 28px;
    line-height: 47px; padding-left: 16px; box-sizing: border-box;
  }
  .info-bar.phone { top: 109px; left: 301px; }
  .info-bar.web { top: 180px; left: 341px; }
  .info-bar.address { top: 251px; left: 381px; }
  .info-icon { position: absolute; }
  .email-band {
    position: absolute; left: 0; bottom: 0; width: 100%; height: 21px;
    background: linear-gradient(180deg, #32c4f2, var(--cyan));
    text-align: center; font-family: "Quicksand", sans-serif; font-size: 16px;
    line-height: 21px; color: #3d5563;
  }
  .ground-shadow { position: absolute; }
</style>
</head>
<body>
<div class="canvas">

  <section class="card-front">
    <div class="brand"><span class="brand-square"></span>KQB PRINTING</div>
    <div class="headline">PRINTING</div>
    <div class="tagline"><span class="accent">THE</span> QUALITY BENCH</div>
    <div class="web-bar">
      <div class="cap"></div>
      <div class="mid">www.kqbprinting.com</div>
      <div class="cap"></div>
    </div>
  </section>
  <svg class="ground-shadow" style="left:340px;top:540px" width="500" height="16">
    <ellipse cx="250" cy="8" rx="245" ry="4" fill="var(--shadow)"/>
  </svg>

  <section class="card-back">
    <svg class="map-panel" width="761" height="433" viewBox="0 0 761 433">
      <defs>
        <linearGradient id="edge-shade" x1="0" y1="0" x2="1" y2="0">
          <stop offset="0" stop-color="#000" stop-opacity="0.45"/>
          <stop offset="1" stop-color="#000" stop-opacity="0"/>
        </linearGradient>
      </defs>
      <polygon points="248,0 276,0 472,412 444,412" fill="url(#edge-shade)"/>
      <g role="img" aria-label="Faint world map behind the contact details">
        <polygon points="0,0 248,0 444,412 0,412" fill="var(--back-panel)"/>
        <polygon points="0,0 248,0 444,412 0,412" fill="var(--map-tone)" opacity="0.35"/>
      </g>
    </svg>

    <div class="brand"><span class="brand-square"></span>KQB PRINTING</div>

    <div class="info-bar phone">731.590.4407</div>
    <div class="info-bar web">www.kqbprinting.com</div>
    <div class="info-bar address">Moravel Dunsbridge</div>

    <svg class="info-icon" style="left:272px;top:117px" width="32" height="32" viewBox="0 0 32 32" aria-label="Phone">
      <circle cx="16" cy="16" r="14" fill="none" stroke="var(--white)" stroke-width="2.5"/>
      <path d="M11 9 l3 0 l1.5 4 l-2 1.5 a10 10 0 0 0 4 4 l1.5 -2 l4 1.5 l0 3 a2 2 0 0 1 -2 2 a13 13 0 0 1 -12 -12 a2 2 0 0 1 2 -2z" fill="var(--white)"/>
    </svg>
    <svg class="info-icon" style="left:310px;top:190px" width="30" height="30" viewBox="0 0 30 30" aria-label="Website">
      <g fill="none" stroke="var(--white)" stroke-width="2">
        <circle cx="15" cy="15" r="12"/>
        <ellipse cx="15" cy="15" rx="5" ry="12"/>
        <line x1="3" y1="15" x2="27" y2="15"/>
        <path d="M5 9 h20 M5 21 h20"/>
      </g>
    </svg>
    <svg class="info-icon" style="left:344px;top:258px" width="30" height="36" viewBox="0 0 30 36" aria-label="Address">
      <ellipse cx="15" cy="31" rx="12" ry="3.5" fill="none" stroke="var(--white)" stroke-width="2"/>
      <path d="M15 2 a9 9 0 0 1 9 9 c0 7 -9 18 -9 18 s-9 -11 -9 -18 a9 9 0 0 1 9 -9z" fill="var(--white)"/>
      <circle cx="15" cy="11" r="3.5" fill="var(--back-dark)"/>
    </svg>

    <div class="email-band">info@kqbprinting.com</div>
  </section>
  <svg class="ground-shadow" style="left:435px;top:1087px" width="390" height="14">
    <ellipse cx="195" cy="7" rx="190" ry="3.5" fill="var(--shadow)"/>
  </svg>

</div>
</body>
</html>
```